Etiketten für Kosmetik Produkte  100% Natural Made in Germany
Etiketten für Kosmetik Produkte 100% Natural Made in Germany
Zielgruppe
auf Hochwertige -zertifizierte Naturprodukte wert legen.
Hergestellt in Deutschland und Verpackt
Aufgabenstellung
Hallo ihr lieben,
für die SilbTau Kosmetik - wünschen wir einen neuen frischen Style - das dunkle Etikett möchten wir los werden.
Ein helles frisches Design
Zielgruppe- alle die auf Hochwertige - zertifizierte Naturprodukte bevorzugen
Die Produkte haben mit eine VERUN Zertifizierung - Höchste Qalität an Naturprodukte
Das Glas was wir nutzen ist ein violettes Glas und sehr hochwertig was wir beibehalten möchten.
Das Produkt ist dadurch sehr Geschütz und nachhaltig dazu
Es sind 12 Produkte - Design bleibt bei allen gleich.
Design Wunsch -!!!!
Was gut zum Glas Passt- nur kein schwarz bitte
und Produkt gut passt
Weiß - Kupfer eventuell
Kein Muss - sind für alles offen ( nur kein schwarz
Logo - Name bleibt :-)
Das Design von Tesoro Naturkosmetik
Gefällt uns sehr gut in der Richtung
Was die Natürlichkeit- Reinheit - Qualität
Verkörpert:-)
Fotos zum Prosukt:
Hier ein link zum Instagram
https://instagram.com/lumaroze.spain?igshid=MzRlODBiNWFlZA==
https://instagram.com/silbtau_naturkosmetik?igshid=MzRlODBiNWFlZA==
An den Flyer den wir hochgeladen kann man sehen um welche Produkte es sich handelt und auch im Instagram zu sehen sind.
Wenn ihr weitere Fotos benötigen tut- bitte melden
Viel Glück :-) danke für eure Unterstützung

```html
<!DOCTYPE html>
<html lang="de">
<head>
<meta charset="utf-8">
<title>SilbTau Naturkosmetik – Etikett Lemon &amp; Orange Oil</title>
<link rel="stylesheet" href="https://fonts.googleapis.com/css2?family=Marcellus&family=Josefin+Sans:wght@300&family=Montserrat:wght@400;700&display=swap">
<style>
  :root {
    --canvas: #ffffff;
    --rim: #c07e57;
    --rim-inner: #e9cdb8;
    --face: #fbf7f1;
    --copper: #a9623c;
    --copper-light: #c98a63;
    --violet: #5a4670;
  }
  html, body {
    margin: 0;
    padding: 0;
    width: 1200px;
    height: 960px;
    overflow: hidden;
    background: var(--canvas);
  }
  .label {
    display: block;
    width: 1200px;
    height: 960px;
  }
  .label__rim { fill: var(--rim); }
  .label__rim-line { fill: none; stroke: var(--rim-inner); stroke-width: 3; }
  .label__face { fill: var(--face); }
  .label__rule { fill: none; stroke: var(--copper-light); stroke-width: 2; }
  .label__dot { fill: var(--copper); }
  .ring-text {
    font-family: "Josefin Sans", sans-serif;
    font-weight: 300;
    font-size: 46px;
    fill: var(--copper);
  }
  .brand-name {
    font-family: "Marcellus", serif;
    font-size: 100px;
    fill: var(--copper);
  }
  .brand-sub {
    font-family: "Marcellus", serif;
    font-size: 44px;
    fill: var(--copper);
  }
  .claim {
    font-family: "Montserrat", sans-serif;
    font-size: 26px;
    fill: var(--violet);
  }
  .claim--bold { font-weight: 700; }
  .claim--light { font-weight: 400; }
  .claim__divider { stroke: var(--violet); stroke-width: 1.5; }
</style>
</head>
<body>
<svg class="label" viewBox="0 0 1200 960" xmlns="http://www.w3.org/2000/svg" aria-label="Etikett SilbTau Naturkosmetik, Lemon &amp; Orange Oil">
  <defs>
    <path id="arc-top" d="M 270 500 A 330 330 0 1 1 930 500"/>
    <path id="arc-bottom" d="M 232 500 A 368 368 0 0 0 968 500"/>
  </defs>

  <circle class="label__rim" cx="600" cy="480" r="440"/>
  <circle class="label__face" cx="600" cy="480" r="405"/>
  <circle class="label__rim-line" cx="600" cy="480" r="395"/>

  <path class="label__rule" d="M 322 460 A 280 280 0 0 1 878 460"/>
  <path class="label__rule" d="M 360 640 A 285 285 0 0 0 862 610"/>

  <text class="ring-text" letter-spacing="14">
    <textPath href="#arc-top" startOffset="50%" text-anchor="middle">LEMON &amp; ORANGE OIL</textPath>
  </text>
  <text class="ring-text" letter-spacing="14">
    <textPath href="#arc-bottom" startOffset="50%" text-anchor="middle">LEMON &amp; ORANGE OIL</textPath>
  </text>

  <circle class="label__dot" cx="225" cy="500" r="9"/>
  <circle class="label__dot" cx="975" cy="500" r="9"/>

  <text class="brand-name" x="600" y="530" text-anchor="middle" letter-spacing="10">SILBTAU</text>
  <text class="brand-sub" x="600" y="598" text-anchor="middle">NATURKOSMETIK</text>

  <text class="claim claim--bold" x="582" y="690" text-anchor="end">BODY CARE</text>
  <line class="claim__divider" x1="604" y1="650" x2="596" y2="708"/>
  <text class="claim claim--light" x="614" y="690" text-anchor="start">ORGANIC</text>
</svg>
</body>
</html>
```